Car wrap desgin Talvin

We’d like new design proposals for passenger cars (KM Dorvane & Brčka Ulvaro eX). Both vehicles are white. I don’t want the entire car to be wrapped in yellow. more informations about us, you will find under: https://www.talviiiin.ch/home

Less is more. Keep it simple, clean, and stylish - and only with yellow ond black as color beside the with car

```html
<!DOCTYPE html>
<html lang="de">
<head>
<meta charset="utf-8">
<title>Talvin – Fahrzeugbeschriftung</title>
<link href="https://fonts.googleapis.com/css2?family=Montserrat:wght@500;700&display=swap" rel="stylesheet">
<style>
  :root {
    --paint-white: #f7f7f6;
    --backdrop: #e9eaea;
    --ink: #1c1d1f;
    --stripe-grey: #d6d8da;
    --signal-yellow: #e7e21f;
    --sill-black: #2a2b2d;
  }
  * { box-sizing: border-box; margin: 0; padding: 0; }
  html, body { width: 1200px; height: 386px; overflow: hidden; }
  body {
    background: var(--backdrop);
    font-family: "Montserrat", sans-serif;
    color: var(--ink);
    position: relative;
  }
  .wrap-panel {
    position: absolute;
    background: var(--paint-white);
    border-radius: 6px;
    overflow: hidden;
  }
  .panel-sedan { left: 40px; top: 110px; width: 500px; height: 180px; }
  .panel-suv { left: 580px; top: 80px; width: 580px; height: 230px; }

  .wordmark {
    position: absolute;
    font-weight: 700;
    letter-spacing: 0.04em;
    line-height: 1;
    white-space: nowrap;
  }
  .tagline {
    position: absolute;
    font-weight: 500;
    letter-spacing: 0.12em;
    text-transform: uppercase;
    white-space: nowrap;
  }
  .panel-sedan .wordmark { left: 40px; top: 40px; font-size: 38px; }
  .panel-sedan .tagline { left: 42px; top: 86px; font-size: 9.5px; }
  .panel-suv .main-mark { left: 40px; top: 58px; font-size: 46px; }
  .panel-suv .tagline { left: 42px; top: 112px; font-size: 11px; }
  .panel-suv .rear-mark { right: 36px; top: 36px; font-size: 14px; }

  .stripe-zone {
    position: absolute;
    background: linear-gradient(90deg,
      rgba(214, 216, 218, 0) 0%,
      var(--stripe-grey) 45%,
      var(--stripe-grey) 68%,
      var(--signal-yellow) 76%,
      var(--signal-yellow) 82%,
      var(--stripe-grey) 90%,
      rgba(214, 216, 218, 0.4) 100%);
    opacity: 0.75;
  }
  .panel-sedan .stripe-zone { left: 190px; top: 118px; width: 290px; height: 40px; }
  .panel-suv .stripe-zone { left: 260px; top: 146px; width: 300px; height: 44px; }
  .rear-zone {
    position: absolute;
    right: 24px; top: 60px; width: 96px; height: 70px;
    background: linear-gradient(180deg, rgba(214, 216, 218, 0) 0%, var(--stripe-grey) 100%);
    opacity: 0.7;
  }
  .sill {
    position: absolute; left: 0; right: 0; bottom: 0; height: 18px;
    background: var(--sill-black);
  }
</style>
</head>
<body>
  <section class="wrap-panel panel-sedan" aria-label="Beschriftung KM Dorvane, Fahrertür">
    <div class="wordmark">TALVIIIN</div>
    <div class="tagline">Haustechnik + Bauspenglerei</div>
    <div class="stripe-zone" role="img" aria-label="Diagonales Streifenmuster in Grau mit zwei gelben Akzentstreifen"></div>
  </section>

  <section class="wrap-panel panel-suv" aria-label="Beschriftung Brčka Ulvaro eX, Seitenansicht">
    <div class="wordmark main-mark">TALVIIIN</div>
    <div class="tagline">Haustechnik + Bauspenglerei</div>
    <div class="wordmark rear-mark">TALVIIIN</div>
    <div class="rear-zone" role="img" aria-label="Graue Diagonalstreifen am Heck"></div>
    <div class="stripe-zone" role="img" aria-label="Diagonales Streifenmuster in Grau mit zwei gelben Akzentstreifen"></div>
    <div class="sill"></div>
  </section>
</body>
</html>
```